Business Card - Harlow Birch

Need Business Card design for company named Harlow Birch. Software development focused mainly on Ardel eKallo & oBix Apps. I've attached our logo with both a black and white background. Please add trademark symbol to logo when using.

```html
<!DOCTYPE html>
<html lang="en">
<head>
<meta charset="utf-8">
<title>Harlow Birch – Business Card</title>
<link href="https://fonts.googleapis.com/css2?family=Open+Sans:wght@400;600;700&display=swap" rel="stylesheet">
<style>
  :root {
    --backdrop: #2e261f;
    --card-red: #d91f2a;
    --card-black: #0b0b0b;
    --accent-yellow: #f9c412;
    --accent-orange: #f7a51c;
    --paper-white: #ffffff;
    --ink-black: #111111;
  }
  * { margin: 0; padding: 0; box-sizing: border-box; }
  html, body {
    width: 1200px; height: 1014px; overflow: hidden;
    background: var(--backdrop);
    font-family: "Open Sans", Arial, sans-serif;
  }
  .stage {
    position: relative; width: 1200px; height: 1014px;
    display: flex; justify-content: center; align-items: center; gap: 80px;
  }
  .card {
    position: relative; width: 400px; height: 700px; overflow: hidden;
    border-radius: 4px;
  }
  .card--back { background: var(--card-red); color: var(--paper-white); }
  .card--front { background: var(--card-black); }

  .contact { position: absolute; top: 56px; left: 44px; right: 40px; }
  .contact__name { font-size: 26px; font-weight: 700; line-height: 1.2; }
  .contact__title { font-size: 21px; color: var(--accent-yellow); margin-bottom: 26px; }
  .contact__lines { list-style: none; font-size: 20px; line-height: 1.45; }
  .contact__lines .gap { margin-top: 14px; }
  .label { color: var(--accent-yellow); }

  .website {
    position: absolute; left: 36px; bottom: 190px;
    font-size: 22px; font-weight: 700; color: var(--ink-black);
    white-space: nowrap;
  }
  .corner-block { position: absolute; right: 0; bottom: 0; }

  .brand {
    position: absolute; left: 0; right: 0; top: 320px;
    display: flex; align-items: center; justify-content: center; gap: 14px;
    color: var(--paper-white); font-size: 40px; font-weight: 700;
  }
  .brand__dot { width: 22px; height: 22px; border-radius: 50%; background: var(--accent-orange); }
  .brand__tm { font-size: 16px; vertical-align: super; }
</style>
</head>
<body>
<main class="stage">
  <section class="card card--back">
    <div class="contact">
      <p class="contact__name">Dana Whitfield</p>
      <p class="contact__title">Manager</p>
      <ul class="contact__lines">
        <li>555-204-7731 <span class="label">Mobile</span></li>
        <li>dana@harlowbirch.com</li>
        <li class="gap">4120 Cedar Row</li>
        <li>Marlow, FL 33901</li>
        <li>555-204-7790 <span class="label">Fax</span></li>
      </ul>
    </div>
    <p class="website">harlowbirch.com</p>
    <svg class="corner-block" width="150" height="300" viewBox="0 0 150 300" aria-hidden="true">
      <path d="M36 0 H150 V300 H0 V36 Q0 0 36 0 Z" fill="var(--accent-yellow)"/>
      <path d="M70 36 H150 V300 H36 V70 Q36 36 70 36 Z" fill="var(--paper-white)"/>
    </svg>
  </section>

  <section class="card card--front">
    <p class="brand"><span class="brand__dot"></span><span>Harlow Birch<span class="brand__tm">™</span></span></p>
  </section>
</main>
</body>
</html>
```